Book cover design for Kiwis handbook to crisscrossing Canada

I need an awesome book cover designed for my upcoming book “Kiwis handbook to Crisscrossing Canada”, featuring the ledgendary Halvorne motorcycle rally.I would like to use the photo supplied.I require an image that can be used for bookcover hardcopy, front, back and spine. I also need design for Ebooks. The book is currently at the editors and I am estimating a page count of 270pages.The book is aimed as a guide for the many Australians that travel to America each year for Halvorne (biggest motorcycle rally in the world). Book size 9x6”

Target Market(s)

Travel, Motorcyclists, Brenton Mayfield,

Font styles to use
Serif
Sans Serif

Colors

Designer to choose colors to be used in the design.

Requirements
Must have
• Title: Kiwis handbook to Crisscrossing Canada ,
• Subtitle: featuring the Ledgendary HALVORNE motorcycle rally.
• Author name: Carol Westby
• Front cober, spine, rear cover(with room to add a blurb about the book.
Nice to have
• Would like to use photo with orange bike at Pillarstone basin. I have many more images if required. Would like to see a bald eagle and possibly American flag colours through the lettering for America.
• “Aussies guide to”, in smaller lettering (highlight the words “Roadtripping America” a bit more).

```html
<!DOCTYPE html>
<html lang="en">
<head>
<meta charset="utf-8">
<title>Kiwis handbook to Crisscrossing Canada — Cover Spread</title>
<link href="https://fonts.googleapis.com/css2?family=Alfa+Slab+One&family=Oswald:wght@600;700&family=Josefin+Sans:wght@700&family=Crimson+Text&display=swap" rel="stylesheet">
<style>
  :root {
    --canvas: #f3f3f3;
    --paper: #ffffff;
    --ink: #1a1a1a;
    --body-ink: #2b2b2b;
    --title-red: #b8202a;
    --title-steel: #d9dde3;
    --title-navy: #1f2a4a;
    --title-edge: #141414;
    --sky: #c9b9b4;
    --rock: #8a5a48;
    --bike-orange: #b5472c;
    --road: #55504e;
  }
  * { box-sizing: border-box; margin: 0; padding: 0; }
  html, body { width: 899px; height: 1200px; overflow: hidden; background: var(--canvas); }
  .stage { position: relative; width: 899px; height: 1200px; }
  .spread {
    position: absolute; left: 0; top: 288px;
    width: 1096px; height: 760px;
    transform: scale(0.8203); transform-origin: 0 0;
    background: var(--paper);
  }
  /* back cover */
  .back-cover { position: absolute; left: 0; top: 0; width: 526px; height: 760px; }
  .back-map {
    position: absolute; left: 136px; top: 42px; width: 242px; height: 148px;
    border-radius: 30px 60px 40px 70px / 40px 30px 70px 50px;
    background: linear-gradient(135deg, var(--title-navy) 0%, #6d7ba3 40%, #f2f2f2 60%, var(--title-red) 100%);
  }
  .blurb {
    position: absolute; left: 44px; top: 222px; width: 420px;
    font-family: "Crimson Text", serif; font-size: 14.4px; line-height: 17px;
    color: var(--body-ink); text-align: justify;
  }
  .blurb p + p { margin-top: 17px; }
  /* spine */
  .spine { position: absolute; left: 526px; top: 0; width: 64px; height: 760px; }
  .spine-text { position: absolute; left: 0; top: 0; width: 64px; height: 760px; }
  .spine-title { font-family: "Oswald", sans-serif; font-weight: 700; font-size: 26px; fill: var(--ink); }
  .spine-author { font-family: "Josefin Sans", sans-serif; font-weight: 700; font-size: 14px; fill: var(--ink); }
  .spine-map {
    position: absolute; left: 14px; top: 706px; width: 34px; height: 22px; border-radius: 6px 10px 8px 12px;
    background: linear-gradient(135deg, var(--title-navy), #f2f2f2 55%, var(--title-red));
  }
  /* front cover */
  .front-cover { position: absolute; left: 590px; top: 0; width: 506px; height: 760px; overflow: hidden; }
  .cover-title { position: absolute; left: 0; top: 0; width: 506px; height: 340px; }
  .subtitle {
    position: absolute; left: 32px; top: 340px; width: 450px;
    font-family: "Oswald", sans-serif; font-weight: 700; font-size: 15.5px; color: var(--ink);
    text-align: center; white-space: nowrap; letter-spacing: 0.1px;
  }
  .cover-photo {
    position: absolute; left: 0; top: 364px; width: 506px; height: 396px;
    background:
      radial-gradient(ellipse at 40% 70%, var(--bike-orange) 0%, rgba(181,71,44,0.6) 22%, transparent 45%),
      linear-gradient(180deg, #e9e2de 0%, var(--sky) 12%, var(--rock) 30%, #6f6a5a 42%, var(--road) 60%, #2a2422 100%);
  }
  .author {
    position: absolute; left: 0; top: 662px; width: 506px; text-align: center;
    font-family: "Josefin Sans", sans-serif; font-weight: 700; font-size: 38px; letter-spacing: 10px;
    color: var(--paper);
  }
</style>
</head>
<body>
<div class="stage">
  <div class="spread">
    <section class="back-cover">
      <div class="back-map" role="img" aria-label="Map outline filled with flag colours and a bald eagle"></div>
      <div class="blurb">
        <p>Lorem ipsum dolor sit amet, consectetur adipiscing elit. Nullam varius sit amet mi eget luctus. Sed nisl arcu, aliquet sed ipsum nec, mollis aliquet ex. Ut auctor aliquet libero, in elementum elit porta et. Fusce placerat augue in quam congue rutrum. Nunc gravida arcu at odio suscipit, consequat eleifend neque pellentesque. Suspendisse consectetur nibh sed orci egestas vulputate. Cras vitae porta eros.</p>
        <p>Etiam vitae placerat magna. Nulla gravida mauris sed libero vestibulum, eu laoreet enim iaculis. Proin eu lectus in velit aliquet facilisis. Suspendisse varius ullamcorper felis id tempor. In vel diam non mi malesuada tempus. Curabitur vestibulum porta sapien, ut gravida quam luctus vel. Suspendisse potenti. Sed ac euismod urna, ac tempus enim. Suspendisse venenatis, enim vel congue blandit, nisl ex pretium dui, vel blandit neque purus sed lacus. Nam porta vulputate venenatis.</p>
      </div>
    </section>

    <section class="spine">
      <svg class="spine-text" viewBox="0 0 64 760">
        <text class="spine-title" transform="translate(23 22) rotate(90)" textLength="470" lengthAdjust="spacingAndGlyphs">KIWIS HANDBOOK TO CRISSCROSSING CANADA</text>
        <text class="spine-author" transform="translate(27 522) rotate(90)" textLength="152" lengthAdjust="spacing">CAROL WESTBY</text>
      </svg>
      <div class="spine-map" role="img" aria-label="Small flag-coloured map emblem"></div>
    </section>

    <section class="front-cover">
      <svg class="cover-title" viewBox="0 0 506 340" aria-label="Kiwis handbook to Crisscrossing Canada">
        <defs>
          <linearGradient id="titleFill" x1="0" y1="0" x2="0" y2="1">
            <stop offset="0" stop-color="var(--title-navy)"/>
            <stop offset="0.35" stop-color="var(--title-steel)"/>
            <stop offset="0.5" stop-color="#ffffff"/>
            <stop offset="0.62" stop-color="var(--title-red)"/>
            <stop offset="0.8" stop-color="var(--title-steel)"/>
            <stop offset="1" stop-color="#7a7f88"/>
          </linearGradient>
          <linearGradient id="steelFill" x1="0" y1="0" x2="0" y2="1">
            <stop offset="0" stop-color="#ffffff"/>
            <stop offset="0.5" stop-color="#9aa0a8"/>
            <stop offset="1" stop-color="#3a3d42"/>
          </linearGradient>
        </defs>
        <g font-family="'Alfa Slab One', serif" stroke="var(--title-edge)" stroke-width="3" paint-order="stroke">
          <text x="51" y="112" font-size="96" textLength="395" lengthAdjust="spacingAndGlyphs" fill="url(#titleFill)">KIWIS</text>
          <text x="130" y="168" font-size="44" textLength="246" lengthAdjust="spacingAndGlyphs" fill="url(#steelFill)">HANDBOOK TO</text>
          <text x="44" y="232" font-size="54" textLength="424" lengthAdjust="spacingAndGlyphs" fill="url(#steelFill)">CRISSCROSSING</text>
          <text x="41" y="326" font-size="100" textLength="435" lengthAdjust="spacingAndGlyphs" fill="url(#titleFill)">CANADA</text>
        </g>
      </svg>
      <div class="subtitle">FEATURING THE LEDGENDARY HALVORNE MOTORCYCLE RALLY</div>
      <div class="cover-photo" role="img" aria-label="Photo of an orange touring motorcycle with a flag on the road at Pillarstone basin"></div>
      <div class="author">CAROL WESTBY</div>
    </section>
  </div>
</div>
</body>
</html>
```